Business card design for holistic health care clinic

We need a double-sided business card design for our holistic health care clinic that integrates our logo design and also its color scheme. My business is called Veluma. It is an integrative medicine clinic. You have already done the logo for me. Please ensure an elegant and upscale design that is not cluttered, but still has all the necessary information (please see below for details).

Target Market(s)

Wellness, fitness, rehabilitation for educated, well-traveled open-minded clients who are focused on natural, organic, balanced and preventive healthcare and lifestyle.

Industry/Entity Type

Medical

Contact Information for Business Card

Modern, clean.

Number of Pages Required

1 page

Font styles to use
Serif
Sans Serif

Colors

Designer to choose colors to be used in the design.

Requirements
Must have
• Logo on one side, all other information on the other side.
• Other information should include:
• Tomas Brevik - DOE, CPT, LMT
• 4120 North Harlow Street
• Austin, TX 78631
• 512 608 2947
• 818 459 7208
• info@VelumaHealth.com
• t.brevik@VelumaHealth.com
Nice to have
• Darker background on front - but not totally black - shaded/dark gray.

```html
<!DOCTYPE html>
<html lang="en">
<head>
<meta charset="utf-8">
<title>Veluma – Business Card</title>
<link rel="stylesheet" href="https://fonts.googleapis.com/css2?family=Work+Sans:wght@400;500;600;700&display=swap">
<style>
  :root {
    --page: #141414;
    --card: #2a2a2c;
    --card-edge: #232325;
    --brand-blue: #1a8fd0;
    --text-light: #f2f2f2;
    --text-muted: #bdbdbd;
    --mark-gray: #d6d6d6;
  }
  * { box-sizing: border-box; margin: 0; padding: 0; }
  html, body {
    width: 1200px; height: 900px; overflow: hidden;
    background: var(--page);
    font-family: "Work Sans", Arial, sans-serif;
  }
  .stage {
    width: 1200px; height: 900px;
    display: flex; flex-direction: column; align-items: center; justify-content: center;
    gap: 40px;
  }
  .card {
    position: relative;
    width: 700px; height: 400px;
    background: radial-gradient(ellipse at 60% 35%, #333335 0%, var(--card) 55%, var(--card-edge) 100%);
    overflow: hidden;
  }
  .card__band {
    position: absolute; left: 0; right: 0; bottom: 0;
    height: 9px; background: var(--brand-blue);
  }

  /* Front */
  .front__brand {
    position: absolute; left: 0; right: 0; top: 120px;
    text-align: center;
  }
  .front__name {
    font-size: 92px; font-weight: 600; letter-spacing: 2px;
    color: var(--mark-gray); line-height: 1;
  }
  .front__tagline {
    margin-top: 10px;
    font-size: 24px; font-weight: 500; letter-spacing: 1px;
    color: var(--text-muted);
  }
  .front__web {
    position: absolute; left: 0; right: 0; bottom: 34px;
    text-align: center; font-size: 16px; letter-spacing: 1.5px;
    color: var(--text-light);
  }
  .accent { color: var(--brand-blue); }

  /* Back */
  .back__identity {
    position: absolute; left: 36px; top: 92px; width: 330px;
  }
  .back__brand-name {
    font-size: 70px; font-weight: 700; line-height: 1;
    color: var(--brand-blue); letter-spacing: 1px;
  }
  .back__tagline {
    margin-top: 8px;
    font-size: 20px; font-weight: 600; color: var(--brand-blue);
  }
  .back__address {
    margin-top: 14px; padding-left: 30px;
    font-size: 17px; line-height: 1.35; color: var(--text-light);
  }
  .back__divider {
    position: absolute; left: 392px; top: 84px;
    width: 2px; height: 200px; background: var(--brand-blue);
  }
  .back__contact {
    position: absolute; left: 420px; top: 92px;
  }
  .person__name {
    font-size: 28px; font-weight: 600; letter-spacing: 2px;
    color: var(--brand-blue); text-transform: uppercase;
  }
  .person__credentials {
    margin-top: 2px; font-size: 17px; letter-spacing: 1px;
    color: var(--text-light);
  }
  .contact-list {
    list-style: none; margin-top: 20px;
  }
  .contact-list__item {
    display: flex; align-items: center; gap: 12px;
    font-size: 17px; line-height: 1.6; color: var(--text-light);
    letter-spacing: 0.5px;
  }
  .contact-list__icon {
    width: 15px; height: 15px; flex: none;
    fill: none; stroke: var(--brand-blue); stroke-width: 2;
  }
  .contact-list__icon--solid { fill: var(--brand-blue); stroke: none; }
</style>
</head>
<body>
<main class="stage">

  <section class="card card--front">
    <div class="front__brand">
      <div class="front__name">VELUMA</div>
      <div class="front__tagline">Integrative Holistic Medicine</div>
    </div>
    <div class="front__web">www.<span class="accent">velumahealth</span>.com</div>
    <div class="card__band"></div>
  </section>

  <section class="card card--back">
    <div class="back__identity">
      <div class="back__brand-name">VELUMA</div>
      <div class="back__tagline">Integrative Holistic Medicine</div>
      <address class="back__address" style="font-style:normal">
        4120 North Harlow Street<br>
        Austin, TX 78631
      </address>
    </div>

    <div class="back__divider"></div>

    <div class="back__contact">
      <div class="person__name">Tomas Brevik</div>
      <div class="person__credentials">DOE, CPT, LMT</div>
      <ul class="contact-list">
        <li class="contact-list__item">
          <svg class="contact-list__icon contact-list__icon--solid" viewBox="0 0 16 16" aria-hidden="true"><path d="M3 1l3 3-1.5 2c1 2 3 4 5 5L11.5 9.5l3 3-2 2.5C6 14 2 10 1 3z"/></svg>
          512 608 2947
        </li>
        <li class="contact-list__item">
          <svg class="contact-list__icon" viewBox="0 0 16 16" aria-hidden="true"><rect x="4" y="1" width="8" height="14" rx="1.5"/><line x1="7" y1="12.5" x2="9" y2="12.5"/></svg>
          818 459 7208
        </li>
        <li class="contact-list__item">
          <svg class="contact-list__icon contact-list__icon--solid" viewBox="0 0 16 16" aria-hidden="true"><path d="M1 3h14v10H1z M1.5 3.5l6.5 5 6.5-5" /></svg>
          info@VelumaHealth.com
        </li>
        <li class="contact-list__item">
          <svg class="contact-list__icon contact-list__icon--solid" viewBox="0 0 16 16" aria-hidden="true"><path d="M1 3h14v10H1z M1.5 3.5l6.5 5 6.5-5" /></svg>
          t.brevik@VelumaHealth.com
        </li>
        <li class="contact-list__item">
          <svg class="contact-list__icon" viewBox="0 0 16 16" aria-hidden="true" style="stroke-width:1.4"><circle cx="8" cy="8" r="6.5"/><ellipse cx="8" cy="8" rx="3" ry="6.5"/><line x1="1.5" y1="8" x2="14.5" y2="8"/></svg>
          www.<span class="accent">velumahealth</span>.com
        </li>
      </ul>
    </div>
    <div class="card__band"></div>
  </section>

</main>
</body>
</html>
```